Business card design needed

We design, manufacture and install kitchen robes vanity etc.
We have a current card that i want to upload that you can base the design around and make suggestions for other design but we need the logo to be unchanged that i will up load along with our current card.

Industry/Entity Type

Business

Contact Information for Business Card

Tallowind Joinery Works
Dorian Calvestri
47 Quarrington Avenue, Marlbrook S.A 5092
dorian@tallowindjoinery.com.au
Lic. No. Bld 582904 Bld 740251

```html
<!DOCTYPE html>
<html lang="en">
<head>
<meta charset="utf-8">
<title>Tallowind Joinery Works – Business Card</title>
<link href="https://fonts.googleapis.com/css2?family=Cabin:wght@400;500;600;700&display=swap" rel="stylesheet">
<style>
  :root {
    --bg: #e9e6e1;
    --card: #1e1f1f;
    --card-light: #2b2c2c;
    --lime: #a4c03c;
    --silver: #c9cbcc;
    --text-light: #e6e6e6;
    --text-grey: #a8abad;
    --faint: rgba(255,255,255,0.07);
  }
  * { box-sizing: border-box; margin: 0; padding: 0; }
  html, body { width: 1200px; height: 785px; overflow: hidden; }
  body {
    background: var(--bg);
    font-family: "Cabin", sans-serif;
    position: relative;
  }
  .card {
    position: absolute;
    width: 540px;
    height: 330px;
    background: radial-gradient(ellipse at 40% 30%, var(--card-light), var(--card) 70%);
    box-shadow: 0 4px 14px rgba(0,0,0,0.25);
    overflow: hidden;
  }
  .card--back { left: 40px; top: 228px; }
  .card--front { left: 620px; top: 228px; }
  .frame-outer {
    position: absolute; inset: 10px;
    border: 3px solid var(--lime);
  }
  .frame-inner {
    position: absolute; inset: 17px;
    border: 3px solid var(--silver);
  }

  /* back */
  .watermark-name {
    position: absolute;
    left: 80px; top: 158px;
    width: 400px;
    text-align: center;
    font-size: 28px; font-weight: 600;
    letter-spacing: 1px;
    line-height: 34px;
    color: var(--faint);
    transform: rotate(-24deg);
    transform-origin: center;
    white-space: nowrap;
  }
  .services {
    position: absolute; left: 70px; top: 50px;
    list-style: none;
  }
  .services__title {
    color: var(--lime); font-weight: 700; font-size: 19px;
    margin-bottom: 2px;
  }
  .services__item {
    display: flex; align-items: center; gap: 12px;
    font-size: 20px; line-height: 25px;
    color: var(--text-light);
  }
  .services__item:nth-child(odd) { color: var(--lime); }
  .services__item svg { width: 34px; height: 12px; }
  .services__item .bullet { fill: var(--silver); }
  .services__item:nth-child(odd) .bullet { fill: var(--lime); }
  .licence {
    position: absolute; right: 44px; bottom: 78px;
    color: var(--lime); font-size: 13px;
  }

  /* front */
  .person {
    position: absolute; left: 44px; top: 95px;
    font-size: 18px; font-weight: 700;
    font-variant: small-caps; letter-spacing: 0.5px;
    color: var(--text-light);
  }
  .person__surname { color: var(--lime); }
  .brand {
    position: absolute; right: 42px; top: 52px;
    display: flex; align-items: center; gap: 10px;
  }
  .brand__mark { width: 16px; height: 16px; background: var(--lime); }
  .brand__name {
    font-size: 20px; font-weight: 500;
    color: var(--text-grey); letter-spacing: 0.3px;
  }
  .contact {
    position: absolute; left: 44px; bottom: 36px;
    list-style: none; font-size: 17px; line-height: 23px;
    color: var(--text-light);
  }
  .contact__line:nth-child(odd) { color: var(--lime); }
  .contact__line:last-child { color: var(--text-light); }
</style>
</head>
<body>

<section class="card card--back" aria-label="Card back">
  <div class="frame-outer"></div>
  <div class="frame-inner"></div>
  <div class="watermark-name">TALLOWIND JOINERY WORKS</div>
  <ul class="services">
    <li class="services__title">Custom Made</li>
    <li class="services__item"><svg viewBox="0 0 34 12"><polygon class="bullet" points="0,12 34,0 34,12"/></svg>Kitchens</li>
    <li class="services__item"><svg viewBox="0 0 34 12"><polygon class="bullet" points="0,12 34,0 34,12"/></svg>Vanities</li>
    <li class="services__item"><svg viewBox="0 0 34 12"><polygon class="bullet" points="0,12 34,0 34,12"/></svg>Laundry</li>
    <li class="services__item"><svg viewBox="0 0 34 12"><polygon class="bullet" points="0,12 34,0 34,12"/></svg>Robes</li>
    <li class="services__item"><svg viewBox="0 0 34 12"><polygon class="bullet" points="0,12 34,0 34,12"/></svg>Entertainment units</li>
    <li class="services__item"><svg viewBox="0 0 34 12"><polygon class="bullet" points="0,12 34,0 34,12"/></svg>Flat packs</li>
  </ul>
  <p class="licence">Lic No. Bld 582904, Bld 740251</p>
</section>

<section class="card card--front" aria-label="Card front">
  <div class="frame-outer"></div>
  <div class="frame-inner"></div>
  <div class="brand">
    <span class="brand__mark"></span>
    <span class="brand__name">TALLOWIND JOINERY WORKS</span>
  </div>
  <p class="person">Dorian <span class="person__surname">Calvestri</span></p>
  <ul class="contact">
    <li class="contact__line">A 47 Quarrington Avenue, Marlbrook S.A 5092</li>
    <li class="contact__line">M 0412 684 305</li>
    <li class="contact__line">P (08) 8294 6130</li>
    <li class="contact__line">F (08) 8294 6138</li>
    <li class="contact__line">E dorian@tallowindjoinery.com.au</li>
    <li class="contact__line">www.tallowindjoinery.com.au</li>
  </ul>
</section>

</body>
</html>
```